Communication Business Card Design

We offer complete cabling solutions
Data Cabling,Fibre Optic, and Cabling Repairs fault finding
Security camera installation
TV Aerial installation
Security alarm installation
QWV

Industry/Entity Type

Business

Contact Information for Business Card

Threadmore Solutions
ABN 52 918 374 260
EMAIL threadmoresolutions.com.au
Mobile 0418362057
Rob Kesler

```html
<!DOCTYPE html>
<html lang="en">
<head>
<meta charset="utf-8">
<title>Threadmore Solutions – Business Card</title>
<link rel="stylesheet" href="https://fonts.googleapis.com/css2?family=Libre+Baskerville:wght@700&family=Arimo:wght@400&family=Questrial&display=swap">
<style>
  :root {
    --page: #e9e6e1;
    --card: #ffffff;
    --ink: #111111;
    --rule: #e03a2a;
    --wire-pink: #d99ab9;
    --wire-blue: #9aa6dc;
    --wire-green: #9fcca7;
    --cable-dark: #5a5a5a;
    --fibre-blue: #bfe0f2;
  }
  * { box-sizing: border-box; margin: 0; padding: 0; }
  html, body { width: 1200px; height: 892px; overflow: hidden; }
  body {
    background: var(--page);
    position: relative;
    font-family: "Arimo", Arial, sans-serif;
    color: var(--ink);
  }
  .card {
    position: absolute;
    width: 540px;
    height: 309px;
    background: var(--card);
    overflow: hidden;
    box-shadow: 0 6px 18px rgba(0,0,0,0.18);
  }
  .card--front { left: 40px; top: 292px; }
  .card--back { left: 620px; top: 292px; }

  .rule {
    position: absolute;
    height: 2px;
    background: var(--rule);
  }
  .card--front .rule { left: 0; right: 50px; top: 40px; }
  .card--back .rule { left: 30px; right: 20px; top: 40px; }

  .brand {
    position: absolute;
    font-family: "Libre Baskerville", Georgia, serif;
    font-weight: 700;
    font-size: 25px;
    letter-spacing: 2.5px;
    white-space: nowrap;
  }
  .card--front .brand { left: 150px; top: 54px; }
  .card--back .brand { left: 170px; top: 52px; }

  .cable-art {
    position: absolute;
    left: 14px;
    top: 100px;
    width: 240px;
    height: 110px;
    border-radius: 6px;
    background: linear-gradient(90deg, var(--cable-dark), #9a9fa8 60%, var(--fibre-blue));
    opacity: 0.6;
  }
  .wire-band {
    position: absolute;
    left: 0;
    right: 0;
    bottom: 0;
    height: 70px;
    background: linear-gradient(90deg, var(--wire-pink), var(--wire-blue) 50%, var(--wire-green));
    opacity: 0.75;
  }
  .card--back .wire-band { height: 80px; }

  .contact {
    position: absolute;
    right: 32px;
    top: 128px;
    text-align: right;
  }
  .contact__name {
    font-family: "Questrial", "Century Gothic", sans-serif;
    font-size: 30px;
    letter-spacing: 1px;
    margin-bottom: 4px;
  }
  .contact__line {
    font-family: "Questrial", "Century Gothic", sans-serif;
    font-size: 19px;
    display: flex;
    justify-content: flex-end;
    align-items: center;
    gap: 8px;
    line-height: 26px;
  }
  .contact__icon { width: 16px; height: 16px; flex: none; }

  .services {
    position: absolute;
    left: 24px;
    top: 92px;
    list-style: none;
    font-size: 14.5px;
    line-height: 19px;
  }
  .services li { display: flex; align-items: center; gap: 3px; white-space: nowrap; }
  .services svg { width: 13px; height: 13px; flex: none; }
</style>
</head>
<body>

<section class="card card--front">
  <div class="rule"></div>
  <h1 class="brand">Threadmore Solutions</h1>

  <div class="cable-art" role="img" aria-label="Illustration of a fibre optic cable end with coloured inner tubes and glowing fibre strands"></div>

  <div class="wire-band" role="img" aria-label="Decorative band of twisted multicoloured wires"></div>

  <div class="contact">
    <p class="contact__name">Rob Kesler</p>
    <p class="contact__line">0418362057
      <svg class="contact__icon" viewBox="0 0 16 16" aria-hidden="true"><rect width="16" height="16" fill="var(--ink)"/><path d="M5 3 L7 3 L7.5 6 L6.3 7 C6.9 8.4 7.8 9.3 9 9.8 L10 8.6 L13 9.2 L13 11.5 C13 12.3 12.3 13 11.5 13 C7 12.6 3.4 9 3 4.5 C3 3.7 4 3 5 3 Z" fill="#fff"/></svg>
    </p>
    <p class="contact__line">threadmoresolutions.com.au
      <svg class="contact__icon" viewBox="0 0 16 16" aria-hidden="true"><rect width="16" height="16" fill="var(--ink)"/><rect x="3" y="4.5" width="10" height="7" fill="#fff"/><path d="M3 4.5 L8 8.5 L13 4.5" fill="none" stroke="var(--ink)" stroke-width="1"/></svg>
    </p>
  </div>
</section>

<section class="card card--back">
  <div class="rule"></div>
  <h2 class="brand">Threadmore Solutions</h2>

  <ul class="services">
    <li><svg viewBox="0 0 14 14" aria-hidden="true"><path d="M1 7 L5 11 L13 2" fill="none" stroke="var(--ink)" stroke-width="2.4"/></svg>Data Cabling,Fibre Optic, and Cabling Repairs fault finding</li>
    <li><svg viewBox="0 0 14 14" aria-hidden="true"><path d="M1 7 L5 11 L13 2" fill="none" stroke="var(--ink)" stroke-width="2.4"/></svg>Security camera installation</li>
    <li><svg viewBox="0 0 14 14" aria-hidden="true"><path d="M1 7 L5 11 L13 2" fill="none" stroke="var(--ink)" stroke-width="2.4"/></svg>TV Aerial installation</li>
    <li><svg viewBox="0 0 14 14" aria-hidden="true"><path d="M1 7 L5 11 L13 2" fill="none" stroke="var(--ink)" stroke-width="2.4"/></svg>Security alarm installation</li>
    <li><svg viewBox="0 0 14 14" aria-hidden="true"><path d="M1 7 L5 11 L13 2" fill="none" stroke="var(--ink)" stroke-width="2.4"/></svg>QWV</li>
  </ul>

  <div class="wire-band" role="img" aria-label="Decorative band of twisted multicoloured wires"></div>
</section>

</body>
</html>
```